International Legal Service Company needs Letterhead Design

Put my new Logo into Letterhead Design, using updated telephone number, e-mail address and website. Current letterhead and updated information which i want you to include my new letterhead attached herewith. Of course, my new Logo attached herein. Also, you can use slogan "Total Legal Outsourcing Solutions For Multinational Businesses"

It Company

```html
<!DOCTYPE html>
<html lang="en">
<head>
<meta charset="utf-8">
<title>Meridian Counsel Partners Inc — Letterhead</title>
<link rel="stylesheet" href="https://fonts.googleapis.com/css2?family=Open+Sans:wght@400;600&display=swap">
<style>
  :root{
    --backdrop:#e9e9e9;
    --paper:#f8f8f8;
    --brand:#34508a;
    --ink:#5a5a5a;
    --ink-light:#7a7a7a;
  }
  html,body{margin:0;padding:0;width:1200px;height:1000px;overflow:hidden;background:var(--backdrop);}
  .letterhead{
    position:absolute;left:296px;top:70px;width:608px;height:860px;
    background:var(--paper);box-shadow:0 2px 10px rgba(0,0,0,.12);
    font-family:"Open Sans",Arial,sans-serif;color:var(--ink);
  }
  .brand{position:absolute;left:268px;top:70px;display:flex;align-items:center;gap:12px;}
  .brand-dot{width:52px;height:52px;border-radius:50%;background:var(--brand);flex:none;}
  .brand-name{font-weight:600;font-size:17px;line-height:19px;color:var(--brand);}
  .letter-body{position:absolute;left:58px;top:180px;width:492px;font-size:9.5px;line-height:14px;}
  .letter-body p{margin:0 0 18px;text-align:justify;}
  .letter-body .salutation{margin-bottom:12px;}
  .signature{
    position:absolute;left:330px;top:600px;width:130px;height:40px;
    background:linear-gradient(90deg,rgba(90,90,90,.08),rgba(90,90,90,.18),rgba(90,90,90,.08));
    border-radius:4px;
  }
  .footer-band{position:absolute;left:0;right:0;top:740px;height:7px;background:var(--brand);}
  .contact{position:absolute;left:0;right:0;top:762px;text-align:center;font-size:8.5px;line-height:15px;color:var(--ink-light);}
  .contact-row{display:flex;justify-content:center;gap:14px;}
  .contact-item{display:inline-flex;align-items:center;gap:4px;white-space:nowrap;}
  .contact-item svg{width:9px;height:9px;fill:var(--brand);}
</style>
</head>
<body>
<main class="letterhead">
  <header class="brand">
    <span class="brand-dot"></span>
    <span class="brand-name">Meridian Counsel<br>Partners Inc</span>
  </header>

  <section class="letter-body">
    <p class="salutation">Dear Client,</p>
    <p>Lorem ipsum dolor sit amet, consectetur adipiscing elit. Nulla sodales nisi vitae Lorem ipsum dolor sit amet, consectetur adipiscing elit. Suspendisse feugiat eros nisl, a facilisis risus eleifend sed. Aliquam mauris enim, fermentum eu lacinia sit amet, laoreet eu leo. Nullam eleifend nulla in libero tristique, ac vulputate odio tincidunt. Etiam non condimentum tortor. Integer suscipit neque nec odio porttitor cursus. Phasellus a sapien blandit, suscipit justo id, condimentum ante. Morbi tristique justo risus, id mattis dui molestie ut. Nullam volutpat ut quam commodo faucibus. Pellentesque urna est, interdum in elit quis, pharetra elementum orci. Nam pharetra velit molestie justo placerat sceleris-que.</p>
    <p>Nulla tincidunt molestie libero vel pretium. Donec condimentum nulla sit amet risus semper imperdi-et. Duis congue eros nec diam blandit, et pellentesque sapien auctor. Curabitur iaculis enim lectus, in imperdiet mauris mattis eget. Etiam ac ornare metus. Mauris risus leo, egestas at dolor a, ultrices adipiscing est. Nunc faucibus scelerisque mollis. Pellentesque aliquet mauris tellus, id dignissim risus viverra et. Mauris venenatis lobortis eros. Nam id diam in ligula malesuada feugiat. Cras turpis felis, aliquet id mauris elementum, feugiat ultricies nisl.</p>
    <p>Nullam auctor venenatis metus, eu pulvinar sapien dapibus non. Cum sociis natoque penatibus et magnis dis parturient montes, nascetur ridiculus mus. Praesent sed lorem eget tortor volutpat dictum vel vel ipsum. Morbi ac mauris sed elit dictum volutpat. Morbi pulvinar non nisl in ultrices. Pellentesque quis mi in risus eleifend adipiscing.</p>
    <p>Best regards,</p>
  </section>

  <div class="signature" role="img" aria-label="Handwritten signature of Kenta Morioka"></div>

  <div class="footer-band"></div>

  <footer class="contact">
    <div class="contact-row">
      <span class="contact-item"><svg viewBox="0 0 10 10"><path d="M5 0a3.5 3.5 0 0 0-3.5 3.5C1.5 6 5 10 5 10s3.5-4 3.5-6.5A3.5 3.5 0 0 0 5 0zm0 5a1.5 1.5 0 1 1 0-3 1.5 1.5 0 0 1 0 3z"/></svg>4180 Harbor Park Drive Suite 300 Lakewood, MD 20912</span>
    </div>
    <div class="contact-row">
      <span class="contact-item"><svg viewBox="0 0 10 10"><path d="M2 0.5l1.6 2.2-1 1.1c.6 1.3 1.6 2.3 2.9 2.9l1.1-1L8.8 7.3 7.6 9.5C3.9 9 1 6.1.5 2.4z"/></svg>240-555-0147</span>
      <span class="contact-item"><svg viewBox="0 0 10 10"><rect x="1" y="3" width="8" height="5.5" rx="1"/><rect x="3" y="0.5" width="4" height="3"/></svg>240-555-0183</span>
      <span class="contact-item"><svg viewBox="0 0 10 10"><path d="M0 2h10v6H0z"/><path d="M0.6 2.4L5 5.6 9.4 2.4" fill="none" stroke="#f8f8f8" stroke-width="1"/></svg>kmorioka@example.com</span>
      <span class="contact-item"><svg viewBox="0 0 10 10"><circle cx="5" cy="5" r="4.5"/></svg>meridiancounsel.example.com</span>
    </div>
  </footer>
</main>
</body>
</html>
```